Copper Sprinter

I'm looking for an advertising banner for a fitness programme I'm releasing on Chatterloop. It needs to be centered around indoor rowing and appeal to both men and women. If you wanted to incorporate an indoor rowing machine, I'd prefer the Veltrax 9 over others.

Fitness

```html
<!DOCTYPE html>
<html lang="en">
<head>
<meta charset="utf-8">
<title>Copper Sprinter – ad banner</title>
<link rel="stylesheet" href="https://fonts.googleapis.com/css2?family=Russo+One&family=Roboto:wght@400;500&family=Tinos&display=swap">
<style>
:root{
  --ink:#000;
  --white:#fff;
  --gold:#c9a53c;
  --grey-band:#b9b9b9;
  --panel-line:#c9ccd1;
  --panel-head:#f5f6f8;
  --toggle:#3cbf5c;
  --link:#365899;
  --muted:#90949c;
  --text:#1d2129;
  --btn-line:#ccd0d5;
}
*{box-sizing:border-box;margin:0;padding:0}
html,body{width:1200px;height:1190px;overflow:hidden;background:var(--white)}
body{position:relative;font-family:"Roboto",Arial,sans-serif;color:var(--text)}

/* hero banner (native size 1044 x 548) */
.hero{position:absolute;width:1044px;height:548px;overflow:hidden;transform-origin:0 0}
.hero-main{left:77px;top:24px}
.hero-photo{position:absolute;inset:0;background:
  radial-gradient(circle at 28% 6%,#f3eef2 0,#bcaebf 14%,transparent 34%),
  radial-gradient(circle at 55% 35%,#8a6a58 0,transparent 30%),
  linear-gradient(160deg,#5a4a55 0%,#2b2628 45%,#151515 100%)}
.hero-bands{position:absolute;left:0;top:0}
.brand-name{position:absolute;left:36px;top:150px;font-family:"Russo One",sans-serif;font-size:52px;color:var(--ink);letter-spacing:1px}
.brand-dot{position:absolute;left:48px;top:70px;width:60px;height:60px;border-radius:50%;background:var(--ink)}
.title{position:absolute;left:25px;top:262px;font-family:"Russo One",sans-serif;font-size:58px;line-height:56px;color:var(--white)}
.subtitle{position:absolute;left:25px;top:398px;font-family:"Russo One",sans-serif;font-size:38px;color:var(--ink)}

/* thumbnails */
.thumb{position:relative;overflow:hidden}
.thumb .hero{left:0;top:0}

/* preview panels */
.panel{position:absolute;border:1px solid var(--panel-line);background:var(--white)}
.panel-head{height:39px;background:var(--panel-head);display:flex;align-items:center;padding-left:11px;font-size:12px;color:#4b4f56}
.toggle{width:27px;height:15px;border-radius:8px;background:var(--toggle);position:relative;margin-right:8px}
.toggle::after{content:"";position:absolute;right:2px;top:2px;width:11px;height:11px;border-radius:50%;background:var(--white)}
.btn{display:inline-block;border:1px solid var(--btn-line);background:#f6f7f9;border-radius:2px;font-size:11px;font-weight:500;color:#4b4f56;padding:3px 7px}
.page-row{display:flex;align-items:center;gap:8px}
.page-mark{width:36px;height:30px;font-family:"Russo One",sans-serif;font-size:7px;display:flex;align-items:flex-end;justify-content:center;color:var(--ink)}
.page-name{font-size:13px;font-weight:500}
.sponsored{font-size:10px;color:var(--muted)}
.stats{display:flex;justify-content:space-between;font-size:9px;color:var(--muted);align-items:center}
.like-dot{display:inline-block;width:12px;height:12px;border-radius:50%;background:#4a7bd8;vertical-align:middle;margin-right:4px}
.actions{display:flex;font-size:11px;font-weight:500;color:#606770}

.right-hand{left:34px;top:606px;width:266px;height:280px}
.right-hand .body{padding:22px 0 0 22px;font-size:10.5px}
.right-hand .h{color:var(--link);font-weight:500;margin-top:14px}
.right-hand .c{color:var(--link)}
.right-hand .d{color:var(--muted);margin:3px 0 7px}

.newsfeed{left:342px;top:606px;width:476px;height:552px}
.newsfeed .card{position:absolute;left:22px;top:62px;width:432px;height:456px;border:1px solid #dddfe2;padding:10px 11px}
.newsfeed .copy{font-size:12px;margin:10px 0 8px;line-height:18px}
.newsfeed .link-box{border:1px solid #dddfe2;border-top:none;margin-top:-1px;padding:10px 11px;position:relative;height:84px}
.newsfeed .hl{font-family:"Tinos",serif;font-size:17px}
.newsfeed .ds{font-size:11px;margin-top:5px}
.newsfeed .cp{font-size:9px;color:var(--muted);margin-top:18px}
.newsfeed .link-box .btn{position:absolute;right:11px;bottom:13px}

.mobile{left:860px;top:606px;width:307px;height:427px}
.mobile .card{position:absolute;left:13px;top:53px;width:281px;height:362px;border:1px solid #dddfe2;padding:8px 9px}
.mobile .copy{font-size:12px;margin:10px 0 8px;line-height:16px}
.mobile .link-box{border:1px solid #dddfe2;border-top:none;padding:8px 8px;position:relative;height:64px}
.mobile .link-box .btn{position:absolute;right:8px;top:18px}
</style>
</head>
<body>

<div class="hero hero-main">
  <div class="hero-photo" role="img" aria-label="Photo: man training on an indoor rowing machine in a dim gym"></div>
  <svg class="hero-bands" width="1044" height="548" viewBox="0 0 1044 548">
    <polygon points="0,219 358,219 372,250 0,250" fill="var(--gold)"/>
    <polygon points="0,250 385,250 435,378 0,378" fill="var(--ink)"/>
    <polygon points="385,250 400,250 458,404 445,404" fill="var(--grey-band)"/>
    <polygon points="0,378 445,378 474,465 0,465" fill="var(--grey-band)"/>
    <polygon points="400,250 412,250 484,463 472,463" fill="var(--ink)"/>
  </svg>
  <div class="brand-name">OARVANE</div>
  <div class="title">COPPER<br>SPRINTER</div>
  <div class="subtitle">6-Week Programme</div>
</div>

<section class="panel right-hand">
  <div class="panel-head"><span class="toggle"></span>Right-Hand</div>
  <div class="body">
    <div class="thumb" style="width:221px;height:115px">
      <div class="hero" style="transform:scale(0.2117)">
        <div class="hero-photo" role="img" aria-label="Photo: man training on an indoor rowing machine"></div>
        <svg class="hero-bands" width="1044" height="548" viewBox="0 0 1044 548"><polygon points="0,219 358,219 372,250 0,250" fill="var(--gold)"/><polygon points="0,250 385,250 435,378 0,378" fill="var(--ink)"/><polygon points="0,378 445,378 474,465 0,465" fill="var(--grey-band)"/><polygon points="400,250 412,250 484,463 472,463" fill="var(--ink)"/></svg>
        <div class="brand-name">OARVANE</div><div class="title">COPPER<br>SPRINTER</div><div class="subtitle">6-Week Programme</div>
      </div>
    </div>
    <div class="h">Your Headline Here</div>
    <div class="c">Your Caption Here</div>
    <div class="d">Lorem ipsum dolor sit amet, consectetur adi...</div>
    <span class="btn">Learn More</span>
  </div>
</section>

<section class="panel newsfeed">
  <div class="panel-head"><span class="toggle"></span>Newsfeed</div>
  <div class="card">
    <div class="page-row">
      <div class="page-mark">OARVANE</div>
      <div><div class="page-name" style="color:var(--link)">YourPageHere</div><div class="sponsored">Sponsored</div></div>
      <span class="btn" style="margin-left:auto">Like Page</span>
    </div>
    <p class="copy">Lorem ipsum dolor sit amet, consectetur adipiscing elit. Etiam quis sollicitudin turpis.</p>
    <div class="thumb" style="width:409px;height:214px">
      <div class="hero" style="transform:scale(0.392)">
        <div class="hero-photo" role="img" aria-label="Photo: man training on an indoor rowing machine"></div>
        <svg class="hero-bands" width="1044" height="548" viewBox="0 0 1044 548"><polygon points="0,219 358,219 372,250 0,250" fill="var(--gold)"/><polygon points="0,250 385,250 435,378 0,378" fill="var(--ink)"/><polygon points="0,378 445,378 474,465 0,465" fill="var(--grey-band)"/><polygon points="400,250 412,250 484,463 472,463" fill="var(--ink)"/></svg>
        <div class="brand-name">OARVANE</div><div class="title">COPPER<br>SPRINTER</div><div class="subtitle">6-Week Programme</div>
      </div>
    </div>
    <div class="link-box">
      <div class="hl">Your Headline Here</div>
      <div class="ds">Your Description Here</div>
      <div class="cp">YOUR CAPTION HERE</div>
      <span class="btn">Learn More</span>
    </div>
    <div class="stats" style="margin-top:10px"><span><span class="like-dot"></span>20</span><span>24 Comments &nbsp; 5 Shares</span></div>
    <div class="actions" style="border-top:1px solid #e5e5e5;margin-top:8px;padding-top:9px;gap:40px"><span>Like</span><span>Comment</span><span>Share</span></div>
  </div>
</section>

<section class="panel mobile">
  <div class="panel-head"><span class="toggle"></span>Mobile</div>
  <div class="card">
    <div class="page-row">
      <div class="page-mark">OARVANE</div>
      <div><div class="page-name">YourPageHere</div><div class="sponsored">Sponsored</div></div>
    </div>
    <p class="copy">Lorem ipsum dolor sit amet, consectetur adipiscing elit. Etiam quis sollicitudin turpis.</p>
    <div class="thumb" style="width:259px;height:136px">
      <div class="hero" style="transform:scale(0.248)">
        <div class="hero-photo" role="img" aria-label="Photo: man training on an indoor rowing machine"></div>
        <svg class="hero-bands" width="1044" height="548" viewBox="0 0 1044 548"><polygon points="0,219 358,219 372,250 0,250" fill="var(--gold)"/><polygon points="0,250 385,250 435,378 0,378" fill="var(--ink)"/><polygon points="0,378 445,378 474,465 0,465" fill="var(--grey-band)"/><polygon points="400,250 412,250 484,463 472,463" fill="var(--ink)"/></svg>
        <div class="brand-name">OARVANE</div><div class="title">COPPER<br>SPRINTER</div><div class="subtitle">6-Week Programme</div>
      </div>
    </div>
    <div class="link-box">
      <div style="font-size:12px;font-weight:500">Your Headline Here</div>
      <div style="font-size:11.5px;color:#606770;margin-top:2px">Your Description Here</div>
      <div style="font-size:10px;color:var(--muted);margin-top:5px">Your Caption Here</div>
      <span class="btn">Learn More</span>
    </div>
    <div class="stats" style="margin-top:10px"><span><span class="like-dot"></span>20</span><span>24 Comments &nbsp; 5 Shares</span></div>
    <div class="actions" style="border-top:1px solid #e5e5e5;margin:8px -9px 0;padding:12px 0 0;justify-content:space-around"><span>Like</span><span>Comment</span><span>Share</span></div>
  </div>
</section>

</body>
</html>
```